Lantern Method of Ascent Programme Graphic

Please refer to attached graphic.
I wish to redesign this graphic to represent a programme of work that we (Quellary) deliver to our customers.
The design represents 9 steps ( 3 steps at each of 3 levels) and is all about implementing the 'Lantern Method of Ascent'

I like the fact that the increasing business growth is evident when you are progressing through the stages, but the current graphic looks dated and the colours are not working.
I would also like to incorporate the LMA logo we have created.

Target Market(s)

IT Sector - businesses looking to grow

Industry/Entity Type

We are a digital marketing company

Requirements
Must have
• Clear, concise design
Should not have
• Design must not be complicated

```html
<!DOCTYPE html>
<html lang="en">
<head>
<meta charset="utf-8">
<title>Lantern Method of Ascent Programme</title>
<link href="https://fonts.googleapis.com/css2?family=Montserrat:wght@500;600&family=Outfit:wght@400;500;600&display=swap" rel="stylesheet">
<style>
  :root{
    --bg:#061741;
    --white:#ffffff;
    --teal-top:#03d8d8;
    --teal-bottom:#029d9c;
    --sky-top:#07aaf2;
    --sky-bottom:#0b63c9;
    --royal-top:#0a40f8;
    --royal-bottom:#1a15b4;
    --teal-label:#17c9d2;
    --sky-label:#0aa7ec;
    --royal-label:#1d3ef2;
    --brand:#1a9bd9;
  }
  *{margin:0;padding:0;box-sizing:border-box}
  html,body{width:1200px;height:675px;overflow:hidden;background:var(--bg)}
  .canvas{position:relative;width:1200px;height:675px;background:var(--bg);font-family:"Outfit",sans-serif;color:var(--white)}
  .brand-panel{position:absolute;left:100px;top:220px;width:172px;text-align:center}
  .method-mark{display:flex;align-items:center;justify-content:center;gap:10px;font-family:"Outfit",sans-serif;font-weight:600;font-size:60px;line-height:1;color:var(--brand);letter-spacing:2px}
  .method-mark .dot{width:16px;height:16px;background:var(--brand)}
  .brand-divider{position:absolute;left:12px;top:149px;width:150px;height:2px;background:var(--brand)}
  .company-name{position:absolute;left:-10px;top:196px;width:192px;font-family:"Outfit",sans-serif;font-weight:600;font-size:40px;line-height:1;color:var(--brand)}
  .diagram{position:absolute;left:0;top:0}
  .axis-label{font-family:"Montserrat",sans-serif;font-weight:600;font-size:16px;letter-spacing:5px;fill:var(--white)}
  .level-title{font-family:"Montserrat",sans-serif;font-weight:500;font-size:21px;fill:var(--white)}
  .step-label{font-family:"Outfit",sans-serif;font-weight:400;font-size:19px;fill:var(--white)}
  .icon{fill:none;stroke:var(--white);stroke-width:1.3;stroke-linecap:round;stroke-linejoin:round}
  .cadence{font-family:"Outfit",sans-serif;font-weight:500;font-size:15.5px;fill:var(--white)}
  .focus{font-family:"Outfit",sans-serif;font-weight:600;font-size:15.5px}
  .focus-teal{fill:var(--teal-label)} .focus-sky{fill:var(--sky-label)} .focus-royal{fill:var(--royal-label)}
  .bracket{fill:none;stroke-width:1.6}
  .bracket-teal{stroke:var(--teal-label)} .bracket-sky{stroke:var(--sky-label)} .bracket-royal{stroke:var(--royal-label)}
</style>
</head>
<body>
<div class="canvas">
  <div class="brand-panel">
    <div class="method-mark"><span class="dot"></span>LMA</div>
    <div class="brand-divider"></div>
    <div class="company-name">Quellary</div>
  </div>

  <svg class="diagram" width="1200" height="675" viewBox="0 0 1200 675">
    <defs>
      <linearGradient id="teal" x1="0" y1="0" x2="0" y2="1"><stop offset="0" stop-color="var(--teal-top)"/><stop offset="1" stop-color="var(--teal-bottom)"/></linearGradient>
      <linearGradient id="sky" x1="0" y1="0" x2="0" y2="1"><stop offset="0" stop-color="var(--sky-top)"/><stop offset="1" stop-color="var(--sky-bottom)"/></linearGradient>
      <linearGradient id="royal" x1="0" y1="0" x2="0" y2="1"><stop offset="0" stop-color="var(--royal-top)"/><stop offset="1" stop-color="var(--royal-bottom)"/></linearGradient>
    </defs>

    <g class="value-axis">
      <line x1="397" y1="540" x2="397" y2="135" stroke="#fff" stroke-width="2"/>
      <polyline points="387,145 397,135 407,145" fill="none" stroke="#fff" stroke-width="2"/>
      <text class="axis-label" transform="translate(384,350) rotate(-90)" text-anchor="middle">BUSINESS VALUE</text>
    </g>

    <g class="level level-foundation">
      <text class="level-title" transform="translate(526,254) rotate(-20)" text-anchor="middle">LANTERN</text>
      <polygon points="426,310 642,235 642,348 426,348" fill="url(#teal)"/>
      <rect x="426" y="351" width="216" height="65" fill="url(#teal)"/>
      <rect x="426" y="418" width="216" height="61" fill="url(#teal)"/>
      <g class="icon" transform="translate(478,300)">
        <circle cx="5" cy="4" r="3"/><circle cx="14" cy="4" r="3"/><circle cx="23" cy="4" r="3"/>
        <circle cx="9" cy="14" r="3"/><circle cx="19" cy="14" r="3"/>
        <path d="M1 27c0-5 3-8 8-8s8 3 8 8M11 27c0-5 3-8 8-8s8 3 8 8"/>
      </g>
      <text class="step-label" x="520" y="321">Personas</text>
      <g class="icon" transform="translate(479,370)">
        <rect x="0" y="0" width="26" height="7" rx="2"/><rect x="0" y="9" width="26" height="7" rx="2"/><rect x="0" y="18" width="26" height="7" rx="2"/>
        <path d="M4 3.5h10M4 12.5h10M4 21.5h10"/><circle cx="21" cy="3.5" r="1"/><circle cx="21" cy="12.5" r="1"/><circle cx="21" cy="21.5" r="1"/>
      </g>
      <text class="step-label" x="520" y="390">Database</text>
      <g class="icon" transform="translate(479,434)">
        <rect x="0" y="0" width="26" height="20" rx="2"/><path d="M13 20v4M8 25h10"/>
        <circle cx="13" cy="10" r="4"/><circle cx="13" cy="10" r="1.3"/>
      </g>
      <text class="step-label" x="521" y="454">Systems</text>
      <g class="bracket bracket-teal">
        <path d="M534 479v20M426 540v-41h216v41"/>
      </g>
      <text class="cadence" x="534" y="525" text-anchor="middle">Numbers that Matter</text>
      <text class="focus focus-teal" x="534" y="544" text-anchor="middle">Foundation Metrics</text>
    </g>

    <g class="level level-tactical">
      <text class="level-title" transform="translate(760,206) rotate(-20)" text-anchor="middle">METHOD</text>
      <polygon points="661,263 877,189 877,311 661,311" fill="url(#sky)"/>
      <rect x="661" y="313" width="216" height="81" fill="url(#sky)"/>
      <rect x="661" y="396" width="216" height="83" fill="url(#sky)"/>
      <g class="icon" transform="translate(716,262)">
        <rect x="0" y="0" width="30" height="14" rx="3"/><path d="M5 5h20M5 9h20"/>
        <path d="M4 16h22a3 3 0 0 1 3 3v6a3 3 0 0 1-3 3H9l-4 4v-4a3 3 0 0 1-3-3v-6"/><path d="M8 21h16M8 25h12"/>
      </g>
      <text class="step-label" x="759" y="282">Messaging</text>
      <g class="icon" transform="translate(717,340)">
        <circle cx="10" cy="7" r="5"/><circle cx="20" cy="9" r="5"/>
        <path d="M1 26c0-6 4-10 9-10M12 27c0-6 3-10 8-10s8 4 8 10z"/>
      </g>
      <text class="step-label" x="759" y="361">Leads</text>
      <g class="icon" transform="translate(717,422)">
        <path d="M28 3H10a5 5 0 0 0 0 10h10a5 5 0 0 1 0 10H2"/>
        <rect x="24" y="0" width="5" height="6" rx="1"/><rect x="0" y="20" width="5" height="6" rx="1"/>
        <rect x="12" y="10" width="5" height="6" rx="1"/>
      </g>
      <text class="step-label" x="759" y="443">Pipeline</text>
      <g class="bracket bracket-sky">
        <path d="M769 479v20M661 540v-41h216v41"/>
      </g>
      <text class="cadence" x="769" y="525" text-anchor="middle">Weekly Scorecard</text>
      <text class="focus focus-sky" x="769" y="544" text-anchor="middle">Tactical Execution</text>
    </g>

    <g class="level level-strategic">
      <text class="level-title" transform="translate(990,152) rotate(-20)" text-anchor="middle">ASCENT</text>
      <polygon points="896,208 1112,134 1112,277 896,277" fill="url(#royal)"/>
      <rect x="896" y="279" width="216" height="99" fill="url(#royal)"/>
      <rect x="896" y="380" width="216" height="99" fill="url(#royal)"/>
      <g class="icon" transform="translate(946,214)">
        <path d="M0 2v30h32"/><rect x="5" y="22" width="4" height="8"/><rect x="12" y="18" width="4" height="12"/><rect x="19" y="14" width="4" height="16"/><rect x="26" y="10" width="4" height="20"/>
        <circle cx="9" cy="6" r="5"/><path d="M14 12l10-6M20 5h5v5"/>
      </g>
      <text class="step-label" x="995" y="239">Sales</text>
      <g class="icon" transform="translate(946,312)">
        <path d="M16 20v-8M16 12c-4 0-6-3-6-6 4 0 6 2 6 6zM16 12c4 0 6-3 6-6-4 0-6 2-6 6z"/>
        <path d="M2 6v10c0 6 6 10 14 12 8-2 14-6 14-12V6"/><path d="M6 30h20"/>
      </g>
      <text class="step-label" x="994" y="336">Nurture</text>
      <g class="icon" transform="translate(946,413)">
        <rect x="0" y="0" width="22" height="28" rx="1"/><path d="M4 5h8v5H4zM4 14h14M4 18h10M4 22h8"/>
        <circle cx="23" cy="22" r="6"/><path d="M27 26l5 5"/>
      </g>
      <text class="step-label" x="994" y="436">Reference</text>
      <g class="bracket bracket-royal">
        <path d="M1004 479v20M896 540v-41h216v41"/>
      </g>
      <text class="cadence" x="1004" y="525" text-anchor="middle">Monthly Scorecard</text>
      <text class="focus focus-royal" x="1004" y="544" text-anchor="middle">Strategic Review</text>
    </g>
  </svg>
</div>
</body>
</html>
```